New Business Card Design Project

Details for my new Business Card Design Project will be added soon. Like a nice simple design

Target Market(s)

Home improvement

Industry/Entity Type

Home Improvement

Contact Information for Business Card

Roofing siding gutters additions garages decks

Requirements
Must have
• Phone 5074629183
• Email morvantgc@quellmail.com

```html
<!DOCTYPE html>
<html lang="en">
<head>
<meta charset="utf-8">
<title>Rowan Pellick – Business Card</title>
<link href="https://fonts.googleapis.com/css2?family=Russo+One&family=Oswald:wght@500&family=Lato:wght@400&display=swap" rel="stylesheet">
<style>
  :root {
    --backdrop: #3a3a3c;
    --paper: #f2f2f4;
    --services-grey: #dcdcde;
    --brand-blue: #134a93;
    --name-blue: #3f9fdc;
    --accent-red: #e31b23;
    --white: #ffffff;
  }
  html, body {
    margin: 0;
    width: 1200px;
    height: 900px;
    overflow: hidden;
    background: var(--backdrop);
  }
  .business-card {
    position: absolute;
    left: 100px;
    top: 165px;
    width: 1000px;
    height: 570px;
    box-shadow: 0 10px 30px rgba(0,0,0,.45);
  }
  .business-card svg { display: block; }
  .services-text {
    font-family: "Russo One", sans-serif;
    fill: var(--services-grey);
  }
  .owner-name {
    font-family: "Oswald", sans-serif;
    font-weight: 500;
    fill: var(--name-blue);
    letter-spacing: 1px;
  }
  .contact-text {
    font-family: "Lato", sans-serif;
    font-size: 29px;
    fill: var(--white);
  }
</style>
</head>
<body>
  <div class="business-card">
    <svg width="1000" height="570" viewBox="0 0 1000 570" xmlns="http://www.w3.org/2000/svg">
      <!-- paper -->
      <rect class="card-paper" width="1000" height="570" fill="var(--paper)"/>

      <!-- services headline -->
      <g class="services-text">
        <text x="215" y="135" font-size="128" textLength="760" lengthAdjust="spacingAndGlyphs">roofing, siding</text>
        <text x="190" y="238" font-size="108" textLength="740" lengthAdjust="spacingAndGlyphs">gutter, additions</text>
        <text x="95" y="340" font-size="108" textLength="880" lengthAdjust="spacingAndGlyphs">handyman services</text>
      </g>

      <!-- lower band -->
      <rect class="contact-band" x="0" y="350" width="1000" height="220" fill="var(--brand-blue)"/>
      <rect class="band-rule" x="0" y="345" width="1000" height="6" fill="var(--accent-red)"/>

      <!-- pointer marker -->
      <polygon class="pointer-frame" points="680,318 862,318 752,432" fill="var(--white)"/>
      <polygon class="pointer-arrow" points="706,333 836,333 754,410" fill="var(--accent-red)"/>

      <!-- name -->
      <text class="owner-name" x="18" y="420" font-size="80">ROWAN PELLICK</text>

      <!-- phone -->
      <g class="contact-phone">
        <rect x="20" y="436" width="28" height="28" rx="6" fill="var(--accent-red)"/>
        <path d="M27 447 q7 -6 14 0 v3 h-3 v-2 h-8 v2 h-3 z M28 452 h12 v7 h-12 z" fill="var(--white)"/>
        <text class="contact-text" x="56" y="461">5074629183</text>
      </g>

      <!-- email -->
      <g class="contact-email">
        <rect x="380" y="488" width="28" height="28" rx="6" fill="var(--accent-red)"/>
        <text x="394" y="509" font-family="Lato, sans-serif" font-size="21" fill="var(--white)" text-anchor="middle">@</text>
        <text class="contact-text" x="416" y="513">morvantgc@quellmail.com</text>
      </g>
    </svg>
  </div>
</body>
</html>
```